Meadowlark Counseling Partners, LLC Needs Modern Business Card Design.

We provide behavioral health services from western Kansas to eastern Kansas. There is an abundance of competition for the services we provide with our main competitor being larger and having significantly more financial resources; however, the quality of services we provide is greater and we have started to catch the attention of the State of Kansas. We had a great logo designed by ArtFolio - this will be used to build upon our brand. The logo (attached) should be used in the card development. We want something unique, modern, but also a card design that clearly states our name, contact info, provides the name and unqiue location of each clinician, etc. Rounded edges, or a unique size, just something that makes our business card stand out from others. I have also uploaded each clinician's name and their unique location and phone number.

Our idea is to have one side be black with our logo. Then, on the other side have business cards for each individual. Plus, we want one card that is "generic" with no specific clinician's name listed so that we can give clients an appointment card when they leave. Some clinicians have two locations - we're open to design and background color, but we have started going with branding colors of black, the yellow in the logo files attached, and sometimes a gray. Our new office has been decorated using this theme.

Target Market(s)

individuals and families in need of behavioral health services; potential professional referral sources; existing referral sources

Industry/Entity Type

Business

Contact Information for Business Card

I attached a Word doc that provides clinician names, credentials and location information specific to each individual.

Font styles to use
Serif

Colors
000000
fbed22
dbdbdb
9d9d9d
c3c3c3

Requirements
Must have
• 1) use of the company logo that has been attached; 2) a template that provides us space to individualize business cards for all of our clinicians; 3) should stick to the colors we are branding with: black, yellow from the logo file, maybe a gray shade and we're open to a suggestion on a shade of white.
Nice to have
• Group discussion culminated in the thought that one side would be black with just our logo - no clinician names, etc. A unique design - rounded edges, unique size, some catchy lay-out would be nice.
Should not have
• Must not be too busy. Should look "clean." The project should stick to branding colors: black, yellow (from the logo file), maybe a gray and shade of white.

```html
<!DOCTYPE html>
<html lang="en">
<head>
<meta charset="utf-8">
<title>Meadowlark Counseling Partners, LLC — Business Card</title>
<link rel="stylesheet" href="https://fonts.googleapis.com/css2?family=Cinzel:wght@500&family=PT+Serif:wght@400;700&display=swap">
<style>
  :root {
    --canvas-bg: #d6d6d6;
    --card-black: #050505;
    --card-sheen: #1c1c1c;
    --brand-yellow: #f7c51a;
    --brand-yellow-light: #fbe022;
    --text-light: #dbdbdb;
  }
  * { margin: 0; padding: 0; box-sizing: border-box; }
  html, body { width: 1200px; height: 1000px; overflow: hidden; }
  body { background: var(--canvas-bg); position: relative; }

  .card {
    position: absolute;
    left: 220px;
    width: 760px;
    border-radius: 22px;
    overflow: hidden;
    background: linear-gradient(125deg, var(--card-black) 0%, var(--card-black) 55%, var(--card-sheen) 62%, var(--card-black) 75%);
    box-shadow: 0 6px 14px rgba(0,0,0,0.35);
  }

  .card--front { top: 50px; height: 432px; }
  .card--back { top: 524px; height: 436px; }

  .brand-name {
    position: absolute;
    left: 0; right: 0;
    top: 168px;
    text-align: center;
    font-family: "Cinzel", serif;
    font-weight: 500;
    color: var(--brand-yellow);
  }
  .brand-name__primary { display: block; font-size: 46px; letter-spacing: 2px; line-height: 1.1; }
  .brand-name__secondary { display: block; font-size: 25px; letter-spacing: 1.5px; line-height: 1.4; }

  .back-accent {
    position: absolute;
    left: 0; top: 93px;
    width: 10px; height: 40px;
    background: var(--brand-yellow);
    border-radius: 0 5px 5px 0;
  }

  .contact {
    position: absolute;
    left: 37px; top: 92px;
    font-family: "PT Serif", serif;
    color: var(--text-light);
    font-size: 17px;
    line-height: 23px;
  }
  .contact__name { font-weight: 700; font-size: 20px; color: var(--brand-yellow-light); }
  .contact__role { margin-bottom: 26px; }
  .contact__address { margin-bottom: 14px; }
  .contact__label, .contact__highlight { color: var(--brand-yellow-light); }

  .back-decoration {
    position: absolute;
    left: 310px; top: 0;
    width: 450px; height: 436px;
  }
</style>
</head>
<body>
  <section class="card card--front" aria-label="Card front">
    <h1 class="brand-name">
      <span class="brand-name__primary">MEADOWLARK</span>
      <span class="brand-name__secondary">COUNSELING PARTNERS, LLC</span>
    </h1>
  </section>

  <section class="card card--back" aria-label="Card back">
    <div class="back-accent"></div>
    <div class="contact">
      <p class="contact__name">Daniel R. Hollis, LP</p>
      <p class="contact__role">President</p>
      <p class="contact__address">418 N. Aster Ave.<br>Wichita, Kansas 67214</p>
      <p><span class="contact__label">P</span>: (316) 555-0182</p>
      <p><span class="contact__label">E</span>: info@youremail.com</p>
      <p>www.<span class="contact__highlight">yourwebsite</span>.com</p>
    </div>
    <svg class="back-decoration" viewBox="0 0 450 436" role="img" aria-label="Large brand mark decoration rising from the lower right corner">
      <defs>
        <linearGradient id="decorationFill" x1="0" y1="0" x2="0.6" y2="1">
          <stop offset="0" stop-color="#fbe022" stop-opacity="0"/>
          <stop offset="0.45" stop-color="#fbd21e" stop-opacity="0.35"/>
          <stop offset="1" stop-color="#f7b51a" stop-opacity="0.85"/>
        </linearGradient>
      </defs>
      <rect x="0" y="0" width="450" height="436" fill="url(#decorationFill)"/>
    </svg>
  </section>
</body>
</html>
```